A specialised Sport management needs a corporate brochure design

We are a specialized company in the management and consultancy of sports events. and need to have a company brochure
We provide the following services;
Event management
Venues management
Production
Ticketing
Consulting
Hospitality
Activity management
Event timing
Branding of event
Event supplies
We need a corporate profile design for our company to showcase the major events that we have covered , with images, information, statistics, surveys, products and services used. We want to highlight our professionalism and execution of the events, experience of the participants, spectators . How we have grown in the past few years and reached the international standards.
Objectives of the work:
To get sponsors and partners for future business and to present Keel-Marrow
as not just a sports management company but also a professional sports
events management company.
You can check our website
www.keel-marrow.example
Target Market(s)
Sponsors and corporate partners
Industry/Entity Type
Events
Font styles to use
Requirements
Must have
- Must Have:
- - Very professional look
- -Some event images,Event information, statistics, surveys, products and services used. We want to highlight our professionalism and execution of the events (Attached)
Nice to have
- Similar momentom of the below design
- http://www.dunlathgames.example/wp-content/themes/dunlath_games/pdf/CP-2014-15-V10-Web.pdf

```html
<!DOCTYPE html>
<html lang="en">
<head>
<meta charset="utf-8">
<title>Keel-Marrow Sport Management – Brochure Cover</title>
<link rel="stylesheet" href="https://fonts.googleapis.com/css2?family=Barlow+Condensed:wght@500;600&family=Barlow+Semi+Condensed:wght@400&display=swap">
<style>
  :root {
    --page: #fdfdfd;
    --edge: #d9d9d9;
    --ink: #383838;
    --ink-soft: #555555;
    --rule: #cfcfcf;
    --icon: #8fb8d8;
    --accent: #1f7a3e;
  }
  * { margin: 0; padding: 0; box-sizing: border-box; }
  html, body { width: 1200px; height: 600px; overflow: hidden; background: var(--page); }
  .spread { position: relative; width: 1200px; height: 600px; border: 1px solid var(--edge); background: var(--page); }
  .fold { position: absolute; left: 600px; top: 0; width: 1px; height: 100%; background: var(--edge); }

  .back-cover { position: absolute; left: 0; top: 0; width: 600px; height: 600px; }
  .brand { position: absolute; left: 72px; top: 418px; display: flex; align-items: center; gap: 6px; }
  .brand-dot { width: 10px; height: 10px; border-radius: 50%; background: var(--accent); }
  .brand-name { font-family: "Barlow Condensed", sans-serif; font-weight: 600; font-size: 19px; letter-spacing: 0.5px; color: var(--ink); }
  .brand-rule { position: absolute; left: 56px; top: 481px; width: 114px; height: 1px; background: var(--rule); }
  .contacts { position: absolute; left: 59px; top: 492px; list-style: none; font-family: "Barlow Semi Condensed", sans-serif; font-size: 11px; color: var(--ink-soft); }
  .contacts li { display: flex; align-items: center; gap: 3px; height: 12.5px; }
  .contacts li.gap { margin-top: 6px; }
  .contacts .icon { width: 7px; height: 7px; border-radius: 50%; background: var(--icon); flex: none; }

  .front-cover { position: absolute; left: 600px; top: 0; width: 600px; height: 600px; }
  .ring { position: absolute; left: 0; top: 0; }
  .headline { position: absolute; left: 142px; top: 236px; font-family: "Barlow Condensed", sans-serif; font-weight: 500; font-size: 52px; line-height: 51px; color: var(--ink); text-transform: uppercase; }
</style>
</head>
<body>
<div class="spread">
  <section class="back-cover">
    <div class="brand">
      <span class="brand-dot"></span>
      <span class="brand-name">KEEL-MARROW</span>
    </div>
    <div class="brand-rule"></div>
    <ul class="contacts">
      <li><span class="icon"></span>985 0100 2200</li>
      <li><span class="icon"></span>965 0300 4400</li>
      <li class="gap"><span class="icon"></span>events@keel-marrow.example</li>
      <li><span class="icon"></span>www.keel-marrow.example</li>
      <li><span class="icon"></span>KMsportevents</li>
    </ul>
  </section>

  <div class="fold"></div>

  <section class="front-cover">
    <svg class="ring" width="600" height="600" viewBox="600 0 600 600">
      <defs>
        <linearGradient id="crowd-run" x1="0" y1="0" x2="0" y2="1">
          <stop offset="0" stop-color="#8fb6d6"/>
          <stop offset="0.35" stop-color="#c9b79a"/>
          <stop offset="1" stop-color="#4a4443"/>
        </linearGradient>
        <linearGradient id="event-collage" x1="0" y1="0" x2="0" y2="1">
          <stop offset="0" stop-color="#b08f78"/>
          <stop offset="0.3" stop-color="#8aa6c2"/>
          <stop offset="0.6" stop-color="#c9a64a"/>
          <stop offset="1" stop-color="#7d5a52"/>
        </linearGradient>
        <linearGradient id="swim-start" x1="0" y1="0" x2="0" y2="1">
          <stop offset="0" stop-color="#6fa3d6"/>
          <stop offset="0.4" stop-color="#b9cfe0"/>
          <stop offset="0.6" stop-color="#2f3b4c"/>
          <stop offset="1" stop-color="#5d7890"/>
        </linearGradient>
      </defs>
      <path role="img" aria-label="Photo of runners crowding a seaside road at a city run" fill="url(#crowd-run)"
        d="M768.9 155.8 A243 243 0 0 1 1135.6 149.4 L1053.1 223.7 A132 132 0 0 0 853.9 227.1 Z"/>
      <path role="img" aria-label="Collage of event photos: climbing, flags, fitness, football, cheer squads and racing" fill="url(#event-collage)"
        d="M1146.5 162.3 A243 243 0 0 1 1146.5 461.7 L1059.0 393.3 A132 132 0 0 0 1059.0 230.7 Z"/>
      <path role="img" aria-label="Photo of triathletes in wetsuits running into the sea at a race start" fill="url(#swim-start)"
        d="M1135.6 474.6 A243 243 0 0 1 768.9 468.2 L853.9 396.9 A132 132 0 0 0 1053.1 400.3 Z"/>
    </svg>
    <h1 class="headline">We are<br>your true<br>partner</h1>
  </section>
</div>
</body>
</html>
```